Fantasy book Stonewake website needs a redesign (Pressly)

My book website at www.stonewakenovel.example needs a redesign. It was originally done in Pressly, so I need someone familiar with that to help make the site more professional and clean looking. Right now it feels too busy.

Industry/Entity Type

It Professional

Requirements
Must have
• Clean lines, easy to read, easy to navigate.
Nice to have
• If there was an easy way for me to blog to the site so I can keep my fans in the know, that would be great.
Should not have
• No cursive script, no flowery overly busy look. I like a clean modern look of a professional author.

```html
<!DOCTYPE html>
<html lang="en">
<head>
<meta charset="utf-8">
<title>Stonewake – Crown of Ash, Book I</title>
<link rel="stylesheet" href="https://fonts.googleapis.com/css2?family=Oswald:wght@400;500;600&family=PT+Sans+Narrow:wght@400;700&display=swap">
<style>
:root{
  --red:#c8141b;
  --red-dark:#8e0c10;
  --ink:#1b1b1b;
  --text:#333;
  --muted:#666;
  --rule:#d8d8d8;
  --panel:#f1f1f1;
  --header:#161616;
  --footer:#1d1d1d;
  --white:#fff;
}
*{box-sizing:border-box;margin:0;padding:0}
html,body{width:1200px;height:2358px;overflow:hidden;background:var(--white)}
body{position:relative;font-family:"PT Sans Narrow",Arial,sans-serif;color:var(--text);font-size:15px}
a{color:inherit;text-decoration:none}
ul{list-style:none}
.abs{position:absolute}
.heading{font-family:"Oswald",sans-serif;font-weight:400;text-transform:uppercase}

/* header */
.site-header{left:0;top:0;width:1200px;height:70px;background:linear-gradient(#2a2a2a,var(--header))}
.brand{left:110px;top:4px;color:var(--white);font-family:"Oswald",sans-serif;font-weight:500;font-size:38px;line-height:44px;letter-spacing:1px;text-transform:uppercase}
.tagline{left:112px;top:48px;color:var(--white);font-family:"Oswald",sans-serif;font-weight:400;font-size:12px;letter-spacing:.5px}
.search{left:837px;top:19px;width:264px;height:28px;background:#ddd;border:1px solid #999;border-radius:3px}
.search svg{position:absolute;right:8px;top:5px}

/* nav */
.main-nav{left:99px;top:70px;width:1002px;height:34px;display:flex;background:linear-gradient(#fafafa,#d9d9d9);border-bottom:1px solid #aaa}
.main-nav a{flex:1;display:flex;align-items:center;justify-content:center;font-family:"Oswald",sans-serif;font-size:15px;color:#222;text-transform:uppercase;border-right:1px solid #b5b5b5}
.main-nav a:last-child{border-right:0}

/* hero */
.sky{left:0;top:104px;width:1200px;height:450px;background:linear-gradient(180deg,#4a4a4a 0%,#9a9a9a 35%,#c9c9c9 55%,#7d7d7d 100%)}
.categories{left:99px;top:104px;width:297px;height:450px;background:rgba(242,242,242,.96)}
.cat-tab{left:126px;top:104px;width:222px;height:66px;background:var(--red);clip-path:polygon(0 0,100% 0,100% 78%,50% 100%,0 78%);color:var(--white);font-size:26px;text-align:center;line-height:60px}
.cat-list{left:99px;top:178px;width:297px}
.cat-list li{height:44px;border-bottom:1px solid #cfcfcf;display:flex;align-items:center;padding-left:28px;font-size:19px;color:#444}
.cat-list li::before{content:"";width:15px;height:15px;border-radius:50%;background:var(--ink);margin-right:16px;box-shadow:inset 0 0 0 4px var(--ink),inset 0 0 0 15px var(--white)}
.hero{left:400px;top:104px;width:701px;height:450px;background:var(--red)}
.hero-book{left:30px;top:70px;width:196px;height:340px;background:linear-gradient(150deg,#2d3b6a,#7a5a8c 45%,#b04a2a 80%,#3a2a3a);box-shadow:6px 6px 14px rgba(0,0,0,.45)}
.hero-title{left:320px;top:108px;color:var(--white);font-size:62px;line-height:70px}
.hero-text{left:320px;top:188px;width:360px;color:var(--white);font-family:"Oswald",sans-serif;font-size:17px;line-height:22px;text-transform:uppercase}
.btn{display:inline-flex;align-items:center;gap:10px;background:var(--ink);color:var(--white);font-family:"Oswald",sans-serif;text-transform:uppercase;padding:0 12px;border-radius:2px}
.hero .btn{position:absolute;left:320px;top:300px;height:42px;font-size:17px}

/* sidebar */
.sidebar{left:113px;top:578px;width:270px}
.sidebar h2{font-size:27px;color:var(--red);line-height:34px;margin-bottom:8px}
.sidebar li{font-size:15px;line-height:40px;color:#333}
.sidebar li::before{content:"»";color:var(--red);margin-right:14px;font-weight:700}
.sidebar .wrap{line-height:22px;padding:9px 0}
.sidebar section{margin-bottom:22px}
.col-rule{left:396px;top:554px;width:1px;height:1030px;background:var(--rule)}

/* posts */
.post{left:417px;width:684px;border-top:1px solid #e2a0a2}
.post h2{font-size:27px;color:var(--red);line-height:36px;padding-top:4px}
.post-meta{font-family:"Oswald",sans-serif;font-size:12px;color:#222;text-transform:uppercase;border-bottom:1px solid #e2a0a2;padding:4px 0 6px;display:flex;gap:24px}
.post-body{font-size:16px;line-height:21px;color:#444;margin-top:12px}
.post-body p{margin-bottom:17px}
.post-figure{float:left;margin:0 12px 4px 0}
.post .btn{position:absolute;right:0;height:30px;font-size:13px}

/* blog posts block */
.blog-tab{left:99px;top:1584px;width:297px;height:44px;background:var(--red);color:var(--ink);font-size:28px;line-height:44px;padding-left:18px}
.blog-tab span{position:absolute;right:22px;color:var(--white)}
.blog-box{left:99px;top:1628px;width:1002px;height:376px;border:1px solid #ddd;border-top:0;box-shadow:0 2px 6px rgba(0,0,0,.12)}
.blog-item{width:430px}
.blog-item h3{font-family:"Oswald",sans-serif;font-weight:500;font-size:16px;color:var(--red);text-transform:uppercase}
.blog-item p{font-size:14px;line-height:18px;color:#333;margin-top:2px}
.blog-item .post-meta{border:0;padding:10px 0 0;font-size:11px}
.blog-item .post-meta span:first-child{color:var(--red)}
.blog-divider{left:20px;width:960px;height:1px;background:var(--rule)}
.more-row{left:40px;top:318px;width:920px;height:30px}
.more-row::before,.more-row::after{content:"";position:absolute;top:14px;width:410px;height:1px;background:#999}
.more-row::before{left:0}.more-row::after{right:0}
.more-row .btn{position:absolute;left:434px;top:0;height:30px;font-size:13px}

/* footer */
.site-footer{left:0;top:2032px;width:1200px;height:326px;background:linear-gradient(#2a2a2a,var(--footer));border-top:4px solid var(--red-dark)}
.foot-col{top:42px}
.foot-col h4{font-family:"Oswald",sans-serif;font-weight:400;font-size:17px;color:var(--red);text-transform:uppercase;height:30px}
.foot-col li{font-size:14px;color:#eee;line-height:33px}
.copy-bar{left:99px;top:2287px;width:1002px;height:47px;background:#3a3a3a;border-radius:24px;display:flex;align-items:center;padding:0 24px;color:#ccc;font-size:13px}
.follow{margin-left:auto;display:flex;align-items:center;gap:9px}
.follow i{width:26px;height:26px;border-radius:50%;background:#e6e6e6;display:block}
.follow b{font-weight:400;margin-right:8px}
</style>
</head>
<body>

<header class="site-header abs">
  <div class="brand abs">Stonewake</div>
  <div class="tagline abs">Crown of Ash: Book I</div>
  <div class="search abs">
    <svg width="16" height="16" viewBox="0 0 16 16"><circle cx="6.5" cy="6.5" r="4.5" fill="none" stroke="#7a0a0e" stroke-width="2"/><line x1="10" y1="10" x2="14.5" y2="14.5" stroke="#7a0a0e" stroke-width="2.5"/></svg>
  </div>
</header>

<div class="sky abs" role="img" aria-label="Dramatic grey storm clouds"></div>

<nav class="main-nav abs">
  <a>Featured Artwork</a><a>Featured Posts</a><a>Links</a><a>Opinions &amp; Concepts</a><a>Preview the Book</a><a>Reviews!</a><a>Who Am I?</a>
</nav>

<aside class="categories abs"></aside>
<div class="cat-tab abs heading">Categories</div>
<ul class="cat-list abs">
  <li>Featured Artwork</li><li>Featured Posts</li><li>Links</li><li>Opinions &amp; Concepts</li><li>Preview the Book</li><li>Reviews!</li><li>Who Am I?</li>
</ul>

<section class="hero abs">
  <div class="hero-book abs" role="img" aria-label="Printed copy of the Stonewake novel with fantasy cover art"></div>
  <h1 class="hero-title abs heading">Actual Books!</h1>
  <p class="hero-text abs">Wow, folks! So here are proof copies of the books! Both dawnsteel and nightsteel editions! We're prepping for launch soon, so stay tuned. You'll be happy you did! Excitedly, -AV</p>
  <a class="btn">More <svg width="14" height="14" viewBox="0 0 14 14"><path d="M4 1l7 6-7 6z" fill="#c8141b"/></svg></a>
</section>

<aside class="sidebar abs">
  <section>
    <h2 class="heading">Recent Posts</h2>
    <ul><li>Actual Books!</li><li>Editor's endorsement!</li><li>Another Review!</li><li>New Cover Art!</li><li>Latest Preview Posted!</li></ul>
  </section>
  <section>
    <h2 class="heading">Recent Comments</h2>
    <ul><li>Tomas Reyes on Latest Preview Posted!</li><li>Admin on First Review In!!!</li><li class="wrap">Admin on 1st Contest Winners Chosen! (got a Free Review Edition!)</li><li>Nils Rowan on First Review In!!!</li><li>Milo Carver on First Review In!!!</li></ul>
  </section>
  <section>
    <h2 class="heading">Archives</h2>
    <ul><li>May 2013</li><li>November 2012</li><li>May 2012</li><li>April 2012</li><li>March 2012</li><li>February 2012</li><li>January 2012</li></ul>
  </section>
</aside>
<div class="col-rule abs"></div>

<article class="post abs" style="top:566px;height:474px">
  <h2 class="heading">Welcome to my site!</h2>
  <div class="post-meta"><span>January 29, 2012</span><span>Admin</span><span>No Comments</span></div>
  <div class="post-body">
    <div class="post-figure" role="img" aria-label="Portrait photo of the author" style="width:149px;height:162px;background:linear-gradient(160deg,#d8d8d8,#8a8a8a)"></div>
    <p>I want to thank everyone for their help and support in launching my first two part novel, Stonewake, Crown of Ash. It's been an amazing road, and you are my biggest motivation to write, for joy comes from sharing.</p>
    <p>The novel started out as a simple story about a small band of mages, but turned into the first part of an epic tale of assassins, dragons, and an adventure spanning millennia. I knew I'd need at least six books to tell this tale, maybe more! When I started writing, I thought I knew what was going to happen. As it turns out, I was mostly wrong. The story became deeper, my characters matured. Along the way some died, and others became pivotal in ways I could not have foreseen.</p>
    <p>I'd like to say I had it all planned, (I do for the sequel!) but the story at times seemed to write itself and I was lucky enough to be the scribe. I am grateful now to be able to share this with all of you.</p>
    <p>I hope to welcome you to a reading experience unlike any other, a story that brings us back to the days of epic adventure, when we let ourselves be taken away to another world so unlike our own, yet with characters that have the same fears and coming-of-age hurdles.</p>
  </div>
  <a class="btn" style="top:432px">More <svg width="12" height="12" viewBox="0 0 14 14"><path d="M4 1l7 6-7 6z" fill="#c8141b"/></svg></a>
</article>

<article class="post abs" style="top:1046px;height:532px">
  <h2 class="heading">Another Review!</h2>
  <div class="post-meta"><span>January 29, 2012</span><span>Admin</span><span>No Comments</span></div>
  <div class="post-body">
    <div class="post-figure" role="img" aria-label="Stonewake book cover art" style="width:172px;height:262px;background:linear-gradient(160deg,#24335e,#6b4f86 50%,#a8452a)"></div>
    <p>Ember Hollow Books: Stonewake Review, by Dorian Hale</p>
    <p>First off, 4.5 out of 5. Now to the review, this book was amazing and very refreshing. It is a true epic fantasy in the tradition of Marrow, Quell, Adair, and Thorne. ( I know there are other great Fantasy writers but these are the ones that I am thinking of now.)</p>
    <p>The story is deep and encompassing, there are twists and turns around each and every corner, some are predictable others are not. The world is also complex with many facets that make it to where you have to learn and grow as your understanding of the story, the world, and the nature of the world changes.</p>
    <p>One thing I did notice about the story is that it takes place in two main locations but that is acceptable as it is the first book of the series and it uses the locations well to build the proper backstory. The story does alternate perspectives, and I believe it does so very well. These changes are either designated by page breaks and follow a scene that clearly indicates a shift in perspective and/or time or they are designated by a new chapter. Both of these serve to progress the story well as they allow the reader to catch up on events from another character's viewpoint. It also allows the reader to fall in love with certain characters and to begin to despise others.</p>
  </div>
  <a class="btn" style="top:500px">More <svg width="12" height="12" viewBox="0 0 14 14"><path d="M4 1l7 6-7 6z" fill="#c8141b"/></svg></a>
</article>

<div class="blog-tab abs heading">Blog Post <span>»</span></div>
<section class="blog-box abs">
  <div class="blog-item abs" style="left:19px;top:22px">
    <h3>1st Free Review Copy Drawing Closed!!!</h3>
    <p>Winners will hear by March 3rd and receive their copies shortly thereafter. Stay tuned, the next drawing will be held March 15th at noon, east coast time. Email info@stonewakenovel.example to enter!</p>
    <div class="post-meta"><span>January 29, 2012</span><span>Admin</span><span>No Comments</span></div>
  </div>
  <div class="blog-item abs" style="left:542px;top:22px">
    <h3>1st Free Review Copy Drawing Closed!!!</h3>
    <p>Winners will hear by March 3rd and receive their copies shortly thereafter. Stay tuned, the next drawing will be held March 15th at noon, east coast time. Email info@stonewakenovel.example to enter!</p>
    <div class="post-meta"><span>January 29, 2012</span><span>Admin</span><span>No Comments</span></div>
  </div>
  <div class="blog-divider abs" style="top:152px"></div>
  <div class="blog-item abs" style="left:19px;top:174px">
    <h3>1st Free Review Copy Drawing Closed!!!</h3>
    <p>Winners will hear by March 3rd and receive their copies shortly thereafter. Stay tuned, the next drawing will be held March 15th at noon, east coast time. Email info@stonewakenovel.example to enter!</p>
    <div class="post-meta"><span>January 29, 2012</span><span>Admin</span><span>No Comments</span></div>
  </div>
  <div class="blog-item abs" style="left:542px;top:174px">
    <h3>1st Free Review Copy Drawing Closed!!!</h3>
    <p>Winners will hear by March 3rd and receive their copies shortly thereafter. Stay tuned, the next drawing will be held March 15th at noon, east coast time. Email info@stonewakenovel.example to enter!</p>
    <div class="post-meta"><span>January 29, 2012</span><span>Admin</span><span>No Comments</span></div>
  </div>
  <div class="more-row abs"><a class="btn">More <svg width="12" height="12" viewBox="0 0 14 14"><path d="M4 1l7 6-7 6z" fill="#c8141b"/></svg></a></div>
</section>

<footer class="site-footer abs">
  <div class="foot-col abs" style="left:118px"><h4>Meta</h4><ul><li>Register</li><li>Log in</li><li>Entries RSS</li><li>Comments RSS</li><li>Pressly.org</li></ul></div>
  <div class="foot-col abs" style="left:318px"><h4>Blogroll</h4><ul><li>Documentation</li><li>Stonewake Preview on Pageleaf.example</li><li>Plugins</li><li>Suggest Ideas</li><li>Support Forum</li></ul></div>
  <div class="foot-col abs" style="left:589px"><h4>&nbsp;</h4><ul><li>Themes</li><li>Pressly Blog</li><li>Pressly Planet</li></ul></div>
  <div class="foot-col abs" style="left:778px"><h4>Quicklinks</h4><ul><li>Featured Artwork</li><li>Featured Posts</li><li>Links</li><li>Opinions &amp; Concepts</li><li>Preview The Book</li></ul></div>
  <div class="foot-col abs" style="left:946px"><h4>&nbsp;</h4><ul><li>Reviews!</li><li>Who Am I?</li></ul></div>
</footer>
<div class="copy-bar abs">
  <span>Copyright (c) 2012, Arlen Voss, All Rights Reserved</span>
  <div class="follow"><b>Follow</b><i></i><i></i><i></i><i></i></div>
</div>

</body>
</html>
```